Wedding Day Custom Wine Label - Tasmanian (Tamar Valley) wine

I am looking for a custom design that will be put on a wine label to commemorate a very good friend's wedding day.

We will need to be able to take the design and print it on to sticker labels that we can put on to wine bottles.

The bride and groom have asked for a simplistic label design (see example image attached). We need two labels. One for "Pinot Noir" wine and the other for "Chardonnay" wine. We would like the label to say:

The Drumwell's
Pinot Noir
2023
Tamar Valley

and for for the other wine variety:

The Drumwell's
Chardonnay
2023
Tamar Valley

smaller text below to say:

13.5% ALC/VOL 750ML
MAREN & JONAS - 31.10.2024

I am happy to consider other variations - the bride & groom would prefer something minimalistic. Elegant and classy.

Target Market(s)

the bride & groom

Requirements
Must have
• Wedding date (31.10.2024). Wine type (Pinot Noir or Chardonnay).
Should not have
• images not essential

```html
<!DOCTYPE html>
<html lang="en">
<head>
<meta charset="utf-8">
<title>The Drumwell's – Wedding Wine Labels</title>
<link rel="stylesheet" href="https://fonts.googleapis.com/css2?family=Lexend:wght@500;600&display=swap">
<style>
  :root {
    --backdrop: #49453f;
    --label-paper: #f8f3df;
    --ink: #1f1c18;
    --illustration-tone: #dcd6c3;
    --illustration-tone-deep: #cbc4ae;
  }
  * { margin: 0; padding: 0; box-sizing: border-box; }
  html, body {
    width: 1200px;
    height: 3000px;
    overflow: hidden;
    background: var(--backdrop);
  }
  .sheet {
    position: relative;
    width: 1200px;
    height: 3000px;
  }
  .wine-label {
    position: absolute;
    left: 215px;
    width: 770px;
    height: 962px;
    background: var(--label-paper);
    color: var(--ink);
    font-family: "Lexend", sans-serif;
    text-align: center;
    overflow: hidden;
  }
  .wine-label--pinot { top: 59px; }
  .wine-label--chardonnay { top: 1090px; }

  .label-brand {
    position: absolute;
    top: 84px;
    left: 0;
    right: 0;
    font-size: 48px;
    font-weight: 600;
    letter-spacing: 1px;
    line-height: 56px;
  }
  .label-illustration {
    position: absolute;
    background: linear-gradient(180deg, var(--illustration-tone), var(--illustration-tone-deep));
  }
  .label-illustration--wide {
    top: 193px;
    left: 0;
    width: 100%;
    height: 186px;
  }
  .label-illustration--centred {
    top: 185px;
    left: 167px;
    width: 464px;
    height: 202px;
  }
  .label-wine-title {
    position: absolute;
    top: 446px;
    left: 0;
    right: 0;
    font-size: 68px;
    font-weight: 600;
    line-height: 68px;
  }
  .label-details {
    position: absolute;
    top: 788px;
    left: 0;
    right: 0;
    font-size: 24px;
    font-weight: 500;
    line-height: 34px;
  }
</style>
</head>
<body>
<main class="sheet">

  <section class="wine-label wine-label--pinot">
    <h2 class="label-brand">THE DRUMWELL'S</h2>
    <div class="label-illustration label-illustration--wide" role="img"
         aria-label="Pencil-style illustration of a rope tied in a heart-shaped knot running across the label"></div>
    <h1 class="label-wine-title">PINOT NOIR<br>TAMAR VALLEY<br>2023</h1>
    <p class="label-details">13.5% ALC/VOL<br>MAREN &amp; JONAS - 31.10.2024<br>750ML</p>
  </section>

  <section class="wine-label wine-label--chardonnay">
    <h2 class="label-brand">THE DRUMWELL'S</h2>
    <div class="label-illustration label-illustration--centred" role="img"
         aria-label="Pencil-style illustration of a rope looped into an infinity symbol"></div>
    <h1 class="label-wine-title">CHARDONNAY<br>TAMAR VALLEY<br>2023</h1>
    <p class="label-details">13.5% ALC/VOL<br>MAREN &amp; JONAS - 31.10.2024<br>750ML</p>
  </section>

</main>
</body>
</html>
```